Run Specialty Brick & Mortar and Ecom site

We use shopify POS and have a crappy shopify webpage. We want to update our webpage to improve the landing page, add a store, add a blog area
you can look at www.copperwrenstride.com to see what we have and
www.mossfinchstride.com and www.quillhare.com to see what we want.

```html
<!DOCTYPE html>
<html lang="en">
<head>
<meta charset="utf-8">
<title>Copperwren Walking &amp; Running Co</title>
<link href="https://fonts.googleapis.com/css2?family=Libre+Baskerville:wght@400;700&family=Lato:wght@400;700&display=swap" rel="stylesheet">
<style>
:root{
  --accent:#5767b6;
  --topbar:#6f7ec0;
  --navy:#1f2437;
  --ink:#222;
  --muted:#666;
  --grey-band:#e3e4e8;
  --star:#f0892a;
  --tag:#e0603f;
  --footer:#1d1d22;
  --white:#fff;
}
*{box-sizing:border-box;margin:0;padding:0}
html,body{width:1200px;height:5080px;overflow:hidden}
body{font-family:"Lato",sans-serif;color:var(--ink);background:var(--white);position:relative}
section,header,footer{position:absolute;left:0;width:1200px}
.abs{position:absolute}
.btn{position:absolute;background:var(--navy);color:#fff;border-radius:20px;font-size:14px;font-weight:700;display:flex;align-items:center;justify-content:center}
.btn-sm{height:28px;padding:0 14px;font-size:11px;border-radius:14px}
.section-title{position:absolute;font-family:"Libre Baskerville",serif;font-size:40px;font-weight:700;color:#1a1a1a}
.section-title span{color:var(--accent);font-weight:400}
.pager{position:absolute;display:flex;gap:8px}
.pager i{width:26px;height:26px;border-radius:50%;display:flex;align-items:center;justify-content:center}
.pager i.on{background:var(--accent)}
.pager i.off{background:#c9c9cf}
.topbar{top:0;height:44px;background:var(--topbar);color:#fff;font-size:12px}
.nav{top:44px;height:78px;background:#fff}
.nav-links{position:absolute;left:102px;top:32px;display:flex;gap:10px;font-size:14px}
.nav-links a{padding:4px 8px;color:#222;text-decoration:none}
.nav-links a.active{background:var(--navy);color:#fff}
.brand{position:absolute;left:528px;top:0;width:140px;height:140px;border-radius:50%;background:#fff;z-index:3;display:flex;align-items:center;justify-content:center;text-align:center;font-family:"Libre Baskerville",serif;font-weight:700;font-size:14px;color:var(--navy);line-height:1.3}
.search{position:absolute;left:728px;top:18px;width:358px;height:48px;border:1.5px solid #bbb;font-size:12px;color:#666;padding:16px 14px}
.hero{top:122px;height:589px}
.hero-img{position:absolute;inset:0;background:linear-gradient(180deg,#3f7fb0 0%,#5e9ac4 35%,#9fb8c6 55%,#b6a58d 72%,#8d7b66 100%)}
.hero h1{position:absolute;left:110px;top:205px;font-family:"Libre Baskerville",serif;font-size:54px;line-height:68px;color:#fff;font-weight:700}
.hero p{position:absolute;left:112px;top:348px;font-size:28px;color:#fff;font-weight:700;letter-spacing:.5px}
.categories{top:711px;height:553px}
.cat{position:absolute;top:154px;width:234px;height:312px;background:#fff;box-shadow:0 2px 10px rgba(0,0,0,.15)}
.cat .ph{position:absolute;left:8px;top:8px;width:218px;height:245px}
.cat .lbl{position:absolute;left:12px;top:272px;font-size:17px}
.cat svg{position:absolute;right:14px;top:275px}
.about{top:1264px;height:529px;background:var(--grey-band)}
.about .ph{position:absolute;left:110px;top:39px;width:449px;height:438px;background:linear-gradient(160deg,#2a3550,#5a5f6e 55%,#8b7f78)}
.about h2{position:absolute;left:643px;top:44px;font-family:"Libre Baskerville",serif;font-size:38px;font-weight:700}
.about h2 span{color:var(--accent);font-weight:400;margin-left:14px}
.about .txt{position:absolute;left:645px;top:110px;width:440px;font-size:12.2px;line-height:28px;color:#444}
.about .txt p+p{margin-top:18px}
.products{top:1793px;height:635px}
.collections{top:3014px;height:634px}
.pcard{position:absolute;top:173px;width:308px;height:379px;background:#fff;box-shadow:0 2px 10px rgba(0,0,0,.15)}
.pcard .ph{position:absolute;left:20px;top:24px;width:268px;height:190px;border-radius:6px}
.pcard .name{position:absolute;left:24px;top:237px;font-size:20px;color:#333}
.pcard .stars{position:absolute;right:14px;top:238px;color:var(--star);font-size:14px;letter-spacing:1px}
.pcard .price{position:absolute;left:24px;top:277px;font-size:24px;color:#111}
.pcard .price s{font-size:16px;color:#555;margin-right:8px}
.pcard .btn{left:22px;top:322px}
.pcard .tools{position:absolute;right:26px;top:48px;width:34px;height:100px;background:#e9e9ec;display:flex;flex-direction:column;align-items:center;justify-content:space-around;padding:6px 0}
.store{top:2428px;height:586px;background:linear-gradient(180deg,#6a6f78,#9a9ea6 50%,#4b4d55)}
.store .box{position:absolute;left:110px;top:91px;width:976px;height:408px;background:#fff;text-align:center}
.store h2{margin-top:74px;font-family:"Libre Baskerville",serif;font-size:38px;font-weight:400;line-height:58px}
.store h2 span{color:var(--accent);font-weight:700}
.store .box p{margin:24px auto 0;width:680px;font-size:15px;line-height:30px;color:#333}
.subscribe{top:3648px;height:483px}
.subscribe .ph{position:absolute;left:0;top:0;width:610px;height:483px;background:linear-gradient(180deg,#e8e8ea,#b4b7bd 45%,#767a84)}
.subscribe .ph2{position:absolute;left:1086px;top:0;width:114px;height:483px;background:linear-gradient(180deg,#c5c2be,#8c8a86)}
.subscribe .panel{position:absolute;left:610px;top:0;width:476px;height:483px;background:#fff}
.subscribe h2{position:absolute;left:36px;top:58px;font-family:"Libre Baskerville",serif;font-size:40px;line-height:56px;font-weight:400}
.subscribe h2 span{color:var(--accent)}
.subscribe .field{position:absolute;left:26px;top:218px;width:428px;height:74px;border:2px solid #aaa;border-radius:40px;font-size:13px;color:#444;padding:28px 26px}
.blog{top:4131px;height:610px}
.bcard{position:absolute;top:152px;width:314px;height:376px;background:#fff;box-shadow:0 2px 10px rgba(0,0,0,.12)}
.bcard .ph{height:212px}
.bcard .tag{position:absolute;left:14px;top:226px;color:var(--tag);font-size:14px}
.bcard h3{position:absolute;left:14px;top:248px;width:290px;font-size:16.5px;font-weight:400;line-height:25px}
.bcard .meta{position:absolute;left:14px;top:324px;font-size:12px;color:#666;display:flex;align-items:center;gap:6px}
footer{top:4741px;height:339px;background:var(--footer);color:#fff}
footer .brand-f{position:absolute;left:131px;top:52px;width:184px;height:184px;border-radius:50%;background:#fff;display:flex;align-items:center;justify-content:center;text-align:center;font-family:"Libre Baskerville",serif;font-weight:700;color:var(--navy);font-size:17px;line-height:1.35}
footer h4{font-size:18px;font-weight:400;margin-bottom:14px}
footer ul{list-style:none;font-size:13px;line-height:24px}
footer .copy{position:absolute;left:0;width:1200px;top:300px;border-top:1px solid #555;padding-top:10px;text-align:center;font-family:"Libre Baskerville",serif;font-size:12px;letter-spacing:.5px}
.contact-row{display:flex;gap:14px;font-size:13px;line-height:26px;margin-bottom:14px}
</style>
</head>
<body>

<header class="topbar">
  <div class="abs" style="left:110px;top:14px;display:flex;align-items:center;gap:10px">
    <svg width="14" height="18" viewBox="0 0 14 18"><path d="M7 0C3 0 0 3 0 7c0 5 7 11 7 11s7-6 7-11c0-4-3-7-7-7z" fill="#fff"/><circle cx="7" cy="7" r="2.6" fill="#6f7ec0"/></svg>
    <span>4180 Cedar Loop, Suite B, Larkfield TX 77000</span>
  </div>
  <div class="abs" style="left:804px;top:14px;display:flex;gap:20px;align-items:center">
    <span>Gift Cards</span>
    <span style="display:flex;gap:5px;align-items:center"><svg width="13" height="13" viewBox="0 0 13 13"><circle cx="6.5" cy="4" r="3" fill="#fff"/><path d="M1 13c0-3 2.5-5 5.5-5s5.5 2 5.5 5z" fill="#fff"/></svg>Account</span>
    <span style="display:flex;gap:5px;align-items:center"><svg width="15" height="15" viewBox="0 0 15 15"><circle cx="7.5" cy="7.5" r="6.5" fill="none" stroke="#fff" stroke-width="1.3"/><text x="7.5" y="11" font-size="9" text-anchor="middle" fill="#fff" font-family="Lato">?</text></svg>Help</span>
  </div>
</header>

<header class="nav">
  <nav class="nav-links">
    <a class="active">Home</a><a>About</a><a>Store</a><a>Blog</a><a>Products</a>
  </nav>
  <div class="search">Search ...
    <svg class="abs" style="right:14px;top:14px" width="18" height="18" viewBox="0 0 18 18"><circle cx="7.5" cy="7.5" r="6" fill="none" stroke="#999" stroke-width="1.4"/><path d="M12 12l5 5" stroke="#999" stroke-width="1.4"/></svg>
  </div>
</header>
<div class="brand">Copperwren<br>Walking &amp;<br>Running Co</div>

<section class="hero">
  <div class="hero-img" role="img" aria-label="Photo of a runner tying her shoe on a rocky shore by the sea"></div>
  <h1>Walking, Running,<br>Everything in Between</h1>
  <p>Personal Service with a Smile</p>
  <div class="btn" style="left:110px;top:406px;width:118px;height:42px">Shop Now</div>
</section>

<section class="categories">
  <h2 class="section-title" style="left:114px;top:76px">Our <span>Categories</span></h2>
  <div class="pager" style="left:1028px;top:82px"><i class="on"><svg width="10" height="10" viewBox="0 0 10 10"><path d="M6.5 1L2.5 5l4 4" stroke="#fff" stroke-width="1.8" fill="none"/></svg></i><i class="off"><svg width="10" height="10" viewBox="0 0 10 10"><path d="M3.5 1l4 4-4 4" stroke="#fff" stroke-width="1.8" fill="none"/></svg></i></div>
  <div class="cat" style="left:110px"><div class="ph" role="img" aria-label="Running shoes on a shoe box in the store" style="background:linear-gradient(180deg,#3c5a7a,#8c8f96 60%,#b9763f)"></div><span class="lbl">Shoes</span><svg width="22" height="14" viewBox="0 0 22 14"><path d="M1 7h19M14 1l6 6-6 6" stroke="#999" stroke-width="2" fill="none"/></svg></div>
  <div class="cat" style="left:358px"><div class="ph" role="img" aria-label="Pairs of running socks" style="background:linear-gradient(180deg,#6e6e70,#c7a98a 55%,#ece8e2)"></div><span class="lbl">Apparel &amp; Socks</span><svg width="22" height="14" viewBox="0 0 22 14"><path d="M1 7h19M14 1l6 6-6 6" stroke="#999" stroke-width="2" fill="none"/></svg></div>
  <div class="cat" style="left:606px"><div class="ph" role="img" aria-label="Four fitness watch screens" style="background:linear-gradient(180deg,#cfcfd2,#5a5a5e 50%,#b6b6ba)"></div><span class="lbl">Electronics</span><svg width="22" height="14" viewBox="0 0 22 14"><path d="M1 7h19M14 1l6 6-6 6" stroke="#999" stroke-width="2" fill="none"/></svg></div>
  <div class="cat" style="left:853px"><div class="ph" role="img" aria-label="Green leash accessory on tree bark" style="background:linear-gradient(180deg,#8a7e70,#4f8a48 50%,#7a6f64)"></div><span class="lbl">Accessories</span><svg width="22" height="14" viewBox="0 0 22 14"><path d="M1 7h19M14 1l6 6-6 6" stroke="#999" stroke-width="2" fill="none"/></svg></div>
</section>

<section class="about">
  <div class="ph" role="img" aria-label="Photo of the two store owners at a race event"></div>
  <h2>About<span>Us</span></h2>
  <div class="txt">
    <p>While Mara was born in the area, Tom got here as fast as he could (when he was 13). They met in the 80's, got married in the 90's and just celebrated 30 years together. Tom played for the Harbor Hawks (nothing impressive, just minor leagues) and we lived all over our great country. After being away from the Greater Larkfield Area, we moved back in mid-2024 and settled near Route 9 &amp; Elm, so we are definitely local!</p>
    <p>We're both active. Mara plays tennis and Tom tries to complete (not very quickly mind you) a full triathlon each year. Our daughter is a marine biology student and our son an architecture major.</p>
  </div>
  <div class="btn" style="left:643px;top:412px;width:118px;height:46px">Read More</div>
</section>

<section class="products">
  <h2 class="section-title" style="left:114px;top:80px">Our <span>Products</span></h2>
  <div class="pager" style="left:1026px;top:86px"><i class="on"><svg width="10" height="10" viewBox="0 0 10 10"><path d="M6.5 1L2.5 5l4 4" stroke="#fff" stroke-width="1.8" fill="none"/></svg></i><i class="off"><svg width="10" height="10" viewBox="0 0 10 10"><path d="M3.5 1l4 4-4 4" stroke="#fff" stroke-width="1.8" fill="none"/></svg></i></div>
  <div class="pcard" style="left:114px"><div class="ph" role="img" aria-label="Multicoloured running shoe" style="background:radial-gradient(ellipse at 50% 55%,#e0564a 0,#3f6fc4 30%,#f2c443 48%,#fff 70%)"></div><span class="name">Trailbend Shoes</span><span class="stars">★★★★★</span><span class="price">$43.00</span><span class="btn btn-sm">Add To Cart</span></div>
  <div class="pcard" style="left:444px"><div class="ph" role="img" aria-label="Black sports watch" style="background:radial-gradient(circle at 45% 50%,#2b2b2e 0,#3d3d40 28%,#fff 50%)"></div>
    <div class="tools"><svg width="16" height="14" viewBox="0 0 16 14"><path d="M1 1h3l2 8h8l1-6H5" stroke="#555" stroke-width="1.3" fill="none"/><circle cx="7" cy="12" r="1.2" fill="#555"/><circle cx="13" cy="12" r="1.2" fill="#555"/></svg><svg width="14" height="12" viewBox="0 0 14 12"><path d="M7 11S1 7 1 3.5A3 3 0 0 1 7 3a3 3 0 0 1 6 .5C13 7 7 11 7 11z" stroke="#555" stroke-width="1.2" fill="none"/></svg><svg width="16" height="10" viewBox="0 0 16 10"><path d="M1 5s3-4 7-4 7 4 7 4-3 4-7 4-7-4-7-4z" stroke="#555" stroke-width="1.2" fill="none"/><circle cx="8" cy="5" r="1.8" fill="#555"/></svg></div>
    <span class="name">Pacewatch</span><span class="stars">★★★★★</span><span class="price"><s>$43.00</s>$34.00</span><span class="btn btn-sm">Shop Now</span></div>
  <div class="pcard" style="left:772px"><div class="ph" role="img" aria-label="White supplement bottle" style="background:radial-gradient(ellipse at 50% 45%,#d8d8dc 0,#f0f0f2 25%,#fff 45%)"></div><span class="name">Brinetab Nutrition</span><span class="stars">★★★★★</span><span class="price">$47.00</span><span class="btn btn-sm">Add To Cart</span></div>
</section>

<section class="store">
  <div class="abs" style="inset:0" role="img" aria-label="Interior of the running store with shoe walls"></div>
  <div class="box">
    <h2>Larkfield County’s independent,<br><span>locally owned running store!</span></h2>
    <p>We offer personal shoe fittings and a variety of accessories to support your fitness effort, like hydration bottles and packs, nutrition gels and powders, injury prevention items and recovery tools, moisture wicking socks, and more!</p>
    <div class="btn" style="left:416px;top:314px;width:144px;height:46px">Visit Our Store</div>
  </div>
</section>

<section class="collections">
  <h2 class="section-title" style="left:112px;top:80px">New <span>Collections</span></h2>
  <div class="pager" style="left:1026px;top:86px"><i class="on"><svg width="10" height="10" viewBox="0 0 10 10"><path d="M6.5 1L2.5 5l4 4" stroke="#fff" stroke-width="1.8" fill="none"/></svg></i><i class="off"><svg width="10" height="10" viewBox="0 0 10 10"><path d="M3.5 1l4 4-4 4" stroke="#fff" stroke-width="1.8" fill="none"/></svg></i></div>
  <div class="pcard" style="left:114px;top:170px"><div class="ph" role="img" aria-label="Purple elastic shoe laces" style="background:radial-gradient(ellipse at 50% 45%,#8a6fb5 0,#c8bcd9 25%,#fff 50%)"></div><span class="name">SnapLaces</span><span class="stars">★★★★★</span><span class="price">$43.00</span><span class="btn btn-sm">Add To Cart</span></div>
  <div class="pcard" style="left:444px;top:170px"><div class="ph" role="img" aria-label="Pair of patterned running socks" style="background:radial-gradient(ellipse at 50% 50%,#62a9c9 0,#e2553a 30%,#fff 55%)"></div>
    <div class="tools"><svg width="16" height="14" viewBox="0 0 16 14"><path d="M1 1h3l2 8h8l1-6H5" stroke="#555" stroke-width="1.3" fill="none"/><circle cx="7" cy="12" r="1.2" fill="#555"/><circle cx="13" cy="12" r="1.2" fill="#555"/></svg><svg width="14" height="12" viewBox="0 0 14 12"><path d="M7 11S1 7 1 3.5A3 3 0 0 1 7 3a3 3 0 0 1 6 .5C13 7 7 11 7 11z" stroke="#555" stroke-width="1.2" fill="none"/></svg><svg width="16" height="10" viewBox="0 0 16 10"><path d="M1 5s3-4 7-4 7 4 7 4-3 4-7 4-7-4-7-4z" stroke="#555" stroke-width="1.2" fill="none"/><circle cx="8" cy="5" r="1.8" fill="#555"/></svg></div>
    <span class="name">Stridewell Socks</span><span class="stars">★★★★★</span><span class="price"><s>$43.00</s>$34.00</span><span class="btn btn-sm">Shop Now</span></div>
  <div class="pcard" style="left:772px;top:170px"><div class="ph" role="img" aria-label="Roll of red kinesiology tape" style="background:radial-gradient(ellipse at 55% 50%,#e5333c 0,#e55a5f 28%,#f3d9d9 42%,#fff 55%)"></div><span class="name">Flexa</span><span class="stars">★★★★★</span><span class="price">$47.00</span><span class="btn btn-sm">Add To Cart</span></div>
</section>

<section class="subscribe">
  <div class="ph" role="img" aria-label="Wall of running shoes on metal shelves"></div>
  <div class="ph2" role="img" aria-label="Store interior detail"></div>
  <div class="panel">
    <h2>Subscribe to<br><span>our Emails</span></h2>
    <div class="field">Enter Email Address</div>
    <div class="btn" style="left:28px;top:316px;width:142px;height:46px">Subscribe</div>
  </div>
</section>

<section class="blog">
  <h2 class="section-title" style="left:114px;top:80px">Our <span>Blog</span></h2>
  <div class="pager" style="left:1018px;top:86px"><i class="on"><svg width="10" height="10" viewBox="0 0 10 10"><path d="M6.5 1L2.5 5l4 4" stroke="#fff" stroke-width="1.8" fill="none"/></svg></i><i class="off"><svg width="10" height="10" viewBox="0 0 10 10"><path d="M3.5 1l4 4-4 4" stroke="#fff" stroke-width="1.8" fill="none"/></svg></i></div>
  <div class="bcard" style="left:110px"><div class="ph" role="img" aria-label="Runner's legs and shoes on a track" style="background:linear-gradient(180deg,#3a3a3e,#6d5c52 60%,#a44b33)"></div><span class="tag">News</span><h3>Why the Right Sports Gear Can Transform Your Performance</h3><div class="meta"><svg width="14" height="14" viewBox="0 0 14 14"><rect x="1" y="2" width="12" height="11" fill="none" stroke="#888"/><path d="M1 5h12" stroke="#888"/></svg>Apr 7,2025 <svg style="margin-left:16px" width="20" height="12" viewBox="0 0 20 12"><rect x="1" y="1" width="18" height="10" fill="none" stroke="#888"/><circle cx="6" cy="6" r="1" fill="#888"/><circle cx="10" cy="6" r="1" fill="#888"/><circle cx="14" cy="6" r="1" fill="#888"/></svg>4 Comments</div></div>
  <div class="bcard" style="left:440px"><div class="ph" role="img" aria-label="Person stretching on a purple exercise mat" style="background:linear-gradient(180deg,#d9c9c2,#c28fb0 55%,#8b5fa0)"></div><span class="tag">News</span><h3>"Fitness Accessories That Will Keep You Motivated</h3><div class="meta"><svg width="14" height="14" viewBox="0 0 14 14"><rect x="1" y="2" width="12" height="11" fill="none" stroke="#888"/><path d="M1 5h12" stroke="#888"/></svg>Apr 9,2025 <svg style="margin-left:16px" width="20" height="12" viewBox="0 0 20 12"><rect x="1" y="1" width="18" height="10" fill="none" stroke="#888"/><circle cx="6" cy="6" r="1" fill="#888"/><circle cx="10" cy="6" r="1" fill="#888"/><circle cx="14" cy="6" r="1" fill="#888"/></svg>4 Comments</div></div>
  <div class="bcard" style="left:770px"><div class="ph" role="img" aria-label="Feet in white socks beside sneakers" style="background:linear-gradient(180deg,#e7e6e4,#cfcbc6 60%,#a9a6a2)"></div><span class="tag">News</span><h3>The Ultimate Guide to Choosing the Best &nbsp;Accessories</h3><div class="meta"><svg width="14" height="14" viewBox="0 0 14 14"><rect x="1" y="2" width="12" height="11" fill="none" stroke="#888"/><path d="M1 5h12" stroke="#888"/></svg>Apr 5,2025 <svg style="margin-left:16px" width="20" height="12" viewBox="0 0 20 12"><rect x="1" y="1" width="18" height="10" fill="none" stroke="#888"/><circle cx="6" cy="6" r="1" fill="#888"/><circle cx="10" cy="6" r="1" fill="#888"/><circle cx="14" cy="6" r="1" fill="#888"/></svg>4 Comments</div></div>
</section>

<footer>
  <div class="brand-f">Copperwren<br>Walking &amp;<br>Running Co</div>
  <div class="abs" style="left:188px;top:256px;display:flex;gap:8px" aria-label="Social links">
    <span style="width:26px;height:26px;border-radius:50%;background:#5767b6;display:block"></span>
    <span style="width:26px;height:26px;border-radius:50%;background:#fff;display:block"></span>
  </div>
  <div class="abs" style="left:385px;top:74px"><h4>Quick Links</h4><ul><li>Home</li><li>About</li><li>Contact</li><li>Store</li><li>Blog</li></ul></div>
  <div class="abs" style="left:564px;top:72px"><h4>Help Links</h4><ul style="line-height:28px"><li>Privacy policy</li><li>Refund policy</li><li>Terms of service</li><li>FAQ,s</li></ul></div>
  <div class="abs" style="left:770px;top:72px;width:340px"><h4>Contact Info</h4>
    <div class="contact-row"><svg width="20" height="20" viewBox="0 0 20 20"><circle cx="10" cy="10" r="10" fill="#fff"/><path d="M10 4a4 4 0 0 0-4 4c0 3 4 8 4 8s4-5 4-8a4 4 0 0 0-4-4z" fill="#1d1d22"/></svg><span>4180 Cedar Loop, Suite B, Larkfield TX 77000</span></div>
    <div class="contact-row"><svg width="20" height="20" viewBox="0 0 20 20"><circle cx="10" cy="10" r="10" fill="#fff"/><path d="M6 5l2 0 1 3-1.5 1a7 7 0 0 0 3.5 3.5l1-1.5 3 1v2c-5 0-9-4-9-9z" fill="#1d1d22"/></svg><span>555-014-2290</span></div>
    <div class="contact-row"><svg width="20" height="20" viewBox="0 0 20 20"><circle cx="10" cy="10" r="10" fill="#fff"/><rect x="5" y="6.5" width="10" height="7" fill="#1d1d22"/><path d="M5 7l5 4 5-4" stroke="#fff" stroke-width="1" fill="none"/></svg><span style="line-height:28px">Monday - Friday, 9:30am - 6:30pm.<br>Saturday, 8:00am - 3:00pm.<br>Sunday, 12:00pm - 4:00pm.</span></div>
  </div>
  <div class="copy">© 2025, Copperwren Walking &amp; Running</div>
</footer>

</body>
</html>
```